Custom Monogramming and Retail gifts

We need a Business Card for a monogramming business that offers many retail gift options. We are a home based business that uses social media (Chatterbook,clipboardly and our website) to sell our products. Our target market is college age, high school, baby gifts.
We want a preppy fun look. Monogramming is very popular in the South

Industry/Entity Type

College

Contact Information for Business Card

Threaded N' Charmed
Custom Monogramming and Gifts
5183 Larkmoor Lane
Marlowby, SC 29981
Mona Prell, Owner
555-214-7390
threadedncharmed.example
threadedncharmed@mailbox.example

```html
<!DOCTYPE html>
<html lang="en">
<head>
<meta charset="utf-8">
<title>Threaded N' Charmed – Business Card</title>
<link rel="stylesheet" href="https://fonts.googleapis.com/css2?family=Kalam:wght@400&display=swap">
<style>
  :root {
    --page-bg: #2a2a2a;
    --card-aqua: #95cdd6;
    --stitch-pink: #e0177a;
    --ink: #141414;
    --banner-dark: #1c1c1c;
  }
  * { box-sizing: border-box; margin: 0; padding: 0; }
  html, body {
    width: 801px;
    height: 1200px;
    overflow: hidden;
    background: var(--page-bg);
  }
  .business-card {
    position: absolute;
    left: 80px;
    top: 40px;
    width: 641px;
    height: 1120px;
    background: var(--card-aqua);
    font-family: "Kalam", cursive;
    font-weight: 400;
    color: var(--ink);
  }
  .stitch-frame {
    position: absolute;
    inset: 20px;
    border: 3px dashed var(--stitch-pink);
  }
  .brand-name {
    position: absolute;
    top: 110px;
    left: 0;
    right: 0;
    text-align: center;
    color: var(--stitch-pink);
    font-size: 84px;
    font-weight: 400;
    line-height: 1.1;
  }
  .brand-banner {
    position: absolute;
    top: 345px;
    left: 95px;
    width: 451px;
    height: 90px;
  }
  .contact-block {
    position: absolute;
    top: 640px;
    left: 30px;
    right: 30px;
    text-align: center;
  }
  .contact-name {
    display: inline-block;
    font-size: 34px;
    font-weight: 400;
    padding: 0 18px 4px;
    border-bottom: 2px dashed var(--stitch-pink);
    margin-bottom: 16px;
  }
  .contact-line {
    font-size: 28px;
    line-height: 57px;
    white-space: nowrap;
  }
</style>
</head>
<body>
  <main class="business-card">
    <div class="stitch-frame"></div>

    <h1 class="brand-name">Threaded<br>N' Charmed</h1>

    <svg class="brand-banner" viewBox="0 0 451 90" role="img" aria-label="Decorative stitched black banner ornament">
      <rect x="0" y="0" width="451" height="90" rx="40" fill="var(--banner-dark)"/>
    </svg>

    <section class="contact-block">
      <p class="contact-name">Threaded N' Charmed</p>
      <p class="contact-line">Custom Monogramming and Gifts</p>
      <p class="contact-line">5183 Larkmoor Lane Marlowby</p>
      <p class="contact-line">SC 29981 Mona Prell</p>
      <p class="contact-line">Owner 555-214-7390</p>
      <p class="contact-line">threadedncharmed.example</p>
      <p class="contact-line">threadedncharmed@mailbox.example</p>
    </section>
  </main>
</body>
</html>
```